Rocket business card

Modern business card design, use of color is good with clean space too.

Things to include on card:

Quote: I add fuel to your optometry practice

- Eyewear Sales
- Admin Duties
- Revenue Collection
- Leadership
- Tech Adoption
- COGS Reduction
- Product Sourcing
-Medical Growth

Dalton Vessey, CEO
Glint Harbor
Text Me! 847-302-1964
dalton@glintharbor.example

```html
<!DOCTYPE html>
<html lang="en">
<head>
<meta charset="utf-8">
<title>Glint Harbor — Business Card</title>
<link rel="stylesheet" href="https://fonts.googleapis.com/css2?family=Lato:wght@400;700;900&display=swap">
<style>
  :root {
    --backdrop: #3a3a3a;
    --orange: #f5a11c;
    --orange-deep: #ef7d22;
    --red: #e03c2f;
    --white: #ffffff;
    --paper: #f4f4f4;
    --ink: #1a1a1a;
    --rule: #c8c8c8;
  }
  * { box-sizing: border-box; margin: 0; padding: 0; }
  html, body {
    width: 1200px; height: 1015px; overflow: hidden;
    background: var(--backdrop);
    font-family: "Lato", sans-serif;
  }
  .stage {
    width: 1200px; height: 1015px;
    display: flex; flex-direction: column; align-items: center; justify-content: center;
    gap: 56px;
  }
  .card {
    width: 760px; height: 434px; position: relative; overflow: hidden;
    box-shadow: 0 10px 30px rgba(0,0,0,.35);
  }

  /* Front */
  .card--front {
    background: radial-gradient(circle at 45% 55%, var(--orange) 0%, var(--orange-deep) 55%, var(--red) 100%);
    color: var(--white);
    display: flex; flex-direction: column; align-items: center; justify-content: center;
    text-align: center;
  }
  .front__halo {
    position: absolute; width: 330px; height: 330px; border-radius: 50%;
    left: 50%; top: 50%; transform: translate(-50%, -50%);
    background: rgba(255, 200, 80, .22);
  }
  .front__brand, .front__tagline, .front__services { position: relative; }
  .front__brand {
    font-size: 62px; font-weight: 400; letter-spacing: 4px; text-transform: uppercase;
    line-height: 1;
  }
  .front__tagline {
    margin-top: 14px; font-size: 17px; font-weight: 900; letter-spacing: .5px;
    text-transform: uppercase;
  }
  .front__services {
    margin-top: 34px; font-size: 18px; line-height: 1.3; list-style: none;
  }
  .front__services li { display: block; }
  .dot { display: inline-block; width: 8px; height: 8px; border-radius: 50%;
    background: var(--white); margin: 0 7px; vertical-align: middle; }

  /* Back */
  .card--back { background: var(--paper); }
  .back__band {
    position: absolute; left: 0; right: 0; bottom: 0; height: 12px;
    background: linear-gradient(90deg, var(--orange), var(--orange-deep));
  }
  .back__logo {
    position: absolute; left: 60px; top: 0; bottom: 12px; width: 360px;
    display: flex; flex-direction: column; align-items: center; justify-content: center; gap: 18px;
  }
  .back__mark {
    width: 96px; height: 96px; border-radius: 50%;
    background: radial-gradient(circle, var(--orange), var(--red));
  }
  .back__brand {
    font-size: 44px; font-weight: 400; letter-spacing: 3px; text-transform: uppercase;
    color: var(--ink); line-height: 1;
  }
  .back__divider {
    position: absolute; left: 448px; top: 40px; height: 280px; width: 1px;
    background: var(--rule);
  }
  .back__contact {
    position: absolute; left: 490px; top: 78px; color: var(--ink);
  }
  .contact__name {
    font-size: 26px; font-weight: 900; text-transform: uppercase; letter-spacing: .5px;
    background: linear-gradient(90deg, var(--orange-deep), var(--red));
    -webkit-background-clip: text; background-clip: text; color: transparent;
  }
  .contact__role { font-size: 19px; margin-top: 2px; }
  .contact__lines { margin-top: 26px; font-size: 19px; line-height: 1.35; }
  .contact__lead { color: var(--red); }
</style>
</head>
<body>
<main class="stage">
  <section class="card card--front" aria-label="Card front">
    <div class="front__halo"></div>
    <h1 class="front__brand">Glint Harbor</h1>
    <p class="front__tagline">I add fuel to your optometry practice</p>
    <ul class="front__services">
      <li>Eyewear Sales<span class="dot"></span>Admin Duties<span class="dot"></span>Revenue Collection</li>
      <li>Leadership<span class="dot"></span>Tech Adoption<span class="dot"></span>COGS Reduction</li>
      <li>Product Sourcing<span class="dot"></span>Medical Growth</li>
    </ul>
  </section>

  <section class="card card--back" aria-label="Card back">
    <div class="back__logo">
      <div class="back__mark"></div>
      <div class="back__brand">Glint Harbor</div>
    </div>
    <div class="back__divider"></div>
    <div class="back__contact">
      <div class="contact__name">Dalton Vessey</div>
      <div class="contact__role">CEO</div>
      <div class="contact__lines">
        <div><span class="contact__lead">Text Me!</span> 847-302-1964</div>
        <div>dalton@glintharbor.example</div>
      </div>
    </div>
    <div class="back__band"></div>
  </section>
</main>
</body>
</html>
```